Post Lockdown Ortho Special

We are running a special for (Ortho) Braces/Clear Aligner (Quorventa), till July 31st 2020. Up to $2,000 off with free Consultation and Xrays.

We need a ad to run in different formats.

Maybe something with: what better time to get braces when you have to wear a mask all the time.

Trying to rebuild our business and get people in for free consultations.

```html
<!DOCTYPE html>
<html lang="en">
<head>
<meta charset="utf-8">
<title>Post Lockdown Ortho Special – Ad Set</title>
<link href="https://fonts.googleapis.com/css2?family=Bebas+Neue&display=swap" rel="stylesheet">
<style>
  :root {
    --page-bg: #e6e6e6;
    --navy: #4a4e74;
    --violet: #6066ae;
    --lavender: #a3a3d2;
    --white: #ffffff;
    --lip-red: #e8475f;
    --glove-blue: #a8dcea;
  }
  html, body {
    margin: 0;
    padding: 0;
    width: 1200px;
    height: 1142px;
    overflow: hidden;
    background: var(--page-bg);
  }
  .ad-set { display: block; width: 1200px; height: 1142px; }
  .display { font-family: 'Bebas Neue', 'Oswald', sans-serif; }
  .headline { fill: var(--white); }
  .offer { fill: var(--navy); text-anchor: middle; }
  .brand-name { fill: var(--navy); }
  .fill-navy { fill: var(--navy); }
  .fill-violet { fill: var(--violet); }
  .fill-lavender { fill: var(--lavender); }
  .fill-white { fill: var(--white); }
  .offer-badge { fill: var(--white); stroke: var(--violet); stroke-width: 7; }
  .brand-dot { fill: var(--violet); }
</style>
</head>
<body>
<svg class="ad-set" viewBox="0 0 1492 1420" xmlns="http://www.w3.org/2000/svg">
  <defs>
    <clipPath id="clip-leaderboard"><rect x="91" y="58" width="1312" height="556"/></clipPath>
    <clipPath id="clip-square"><rect x="88" y="690" width="667" height="667"/></clipPath>
    <clipPath id="clip-portrait"><rect x="867" y="690" width="538" height="667"/></clipPath>
    <linearGradient id="smile-tones" x1="0" y1="0" x2="1" y2="1">
      <stop offset="0" stop-color="var(--lip-red)"/>
      <stop offset="0.55" stop-color="#f4a3b0"/>
      <stop offset="1" stop-color="var(--glove-blue)"/>
    </linearGradient>
  </defs>

  <!-- Wide leaderboard -->
  <g class="ad ad-leaderboard display" clip-path="url(#clip-leaderboard)">
    <rect class="fill-lavender" x="91" y="58" width="1312" height="556"/>
    <path class="fill-white" d="M91,410 C300,390 600,470 800,614 L91,614 Z"/>
    <path class="fill-violet" d="M91,58 H1403 V560 C1100,520 800,400 91,180 Z"/>
    <path class="fill-navy" d="M91,58 H1403 V480 C1100,440 700,250 91,130 Z"/>

    <circle class="fill-navy" cx="340" cy="265" r="196"/>
    <circle class="offer-badge" cx="370" cy="265" r="186"/>
    <text class="offer" x="370" y="163" font-size="54">UP TO</text>
    <text class="offer" x="368" y="214" font-size="60">$2,000<tspan font-size="34" dx="6" dy="-18">OFF</tspan></text>
    <text class="offer" x="370" y="272" font-size="54" textLength="198" lengthAdjust="spacingAndGlyphs">WITH FREE</text>
    <text class="offer" x="370" y="313" font-size="42" textLength="198" lengthAdjust="spacingAndGlyphs">CONSULTATION</text>
    <text class="offer" x="370" y="366" font-size="54" textLength="198" lengthAdjust="spacingAndGlyphs">AND XRAYS</text>
    <text class="offer" x="370" y="401" font-size="32" textLength="200" lengthAdjust="spacingAndGlyphs">TILL JULY 31<tspan font-size="16" dy="-12">ST</tspan><tspan dy="12"> 2020</tspan></text>

    <text class="headline" x="612" y="202" font-size="112" textLength="714" lengthAdjust="spacingAndGlyphs">WHAT BETTER TIME</text>
    <text class="headline" x="612" y="334" font-size="136" textLength="714" lengthAdjust="spacingAndGlyphs">TO GET BRACES</text>
    <text class="headline" x="612" y="391" font-size="44" textLength="714" lengthAdjust="spacingAndGlyphs">WHEN YOU HAVE TO WEAR A MASK ALL THE TIME</text>

    <rect x="795" y="415" width="505" height="199" rx="90" fill="url(#smile-tones)" role="img" aria-label="Illustration of a smiling mouth with a gloved hand holding a dental mirror"/>

    <g class="brand">
      <circle class="brand-dot" cx="205" cy="515" r="28"/>
      <text class="brand-name" x="278" y="518" font-size="40" textLength="228" lengthAdjust="spacingAndGlyphs">PINECREST FAMILY DENTISTRY</text>
      <text class="brand-name" x="278" y="552" font-size="22" textLength="150" lengthAdjust="spacingAndGlyphs">DR MARIAN HOLLOWAY</text>
    </g>
  </g>

  <!-- Square -->
  <g class="ad ad-square display" clip-path="url(#clip-square)">
    <rect class="fill-lavender" x="88" y="690" width="667" height="667"/>
    <path class="fill-white" d="M88,1050 C350,980 600,1120 755,1190 V1357 H88 Z"/>
    <path class="fill-violet" d="M88,690 H755 V1110 C600,1040 400,1000 88,1005 Z"/>
    <path class="fill-navy" d="M88,690 H755 V860 C500,870 300,950 88,1000 Z"/>

    <circle class="offer-badge" cx="240" cy="1157" r="180"/>
    <text class="offer" x="238" y="1055" font-size="54">UP TO</text>
    <text class="offer" x="236" y="1107" font-size="60">$2,000<tspan font-size="34" dx="6" dy="-18">OFF</tspan></text>
    <text class="offer" x="238" y="1162" font-size="54" textLength="192" lengthAdjust="spacingAndGlyphs">WITH FREE</text>
    <text class="offer" x="238" y="1202" font-size="42" textLength="192" lengthAdjust="spacingAndGlyphs">CONSULTATION</text>
    <text class="offer" x="238" y="1252" font-size="54" textLength="192" lengthAdjust="spacingAndGlyphs">AND XRAYS</text>
    <text class="offer" x="238" y="1286" font-size="32" textLength="194" lengthAdjust="spacingAndGlyphs">TILL JULY 31<tspan font-size="16" dy="-12">ST</tspan><tspan dy="12"> 2020</tspan></text>

    <text class="headline" x="144" y="806" font-size="84" textLength="546" lengthAdjust="spacingAndGlyphs">WHAT BETTER TIME</text>
    <text class="headline" x="144" y="904" font-size="104" textLength="546" lengthAdjust="spacingAndGlyphs">TO GET BRACES</text>
    <text class="headline" x="144" y="951" font-size="35" textLength="546" lengthAdjust="spacingAndGlyphs">WHEN YOU HAVE TO WEAR A MASK ALL THE TIME</text>

    <rect x="430" y="975" width="325" height="220" rx="80" fill="url(#smile-tones)" role="img" aria-label="Illustration of a smiling mouth with a gloved hand holding a dental mirror"/>

    <g class="brand">
      <circle class="brand-dot" cx="478" cy="1265" r="24"/>
      <text class="brand-name" x="537" y="1266" font-size="30" textLength="172" lengthAdjust="spacingAndGlyphs">PINECREST FAMILY DENTISTRY</text>
      <text class="brand-name" x="537" y="1294" font-size="18" textLength="120" lengthAdjust="spacingAndGlyphs">DR MARIAN HOLLOWAY</text>
    </g>
  </g>

  <!-- Portrait -->
  <g class="ad ad-portrait display" clip-path="url(#clip-portrait)">
    <rect class="fill-lavender" x="867" y="690" width="538" height="667"/>
    <path class="fill-white" d="M867,1000 C1000,940 1200,980 1405,950 V1357 H867 Z"/>
    <path class="fill-violet" d="M867,690 H1405 V970 C1200,930 1000,880 867,940 Z"/>
    <path class="fill-navy" d="M867,690 H1405 V770 C1300,850 1100,875 867,880 Z"/>

    <circle class="offer-badge" cx="1258" cy="1092" r="152"/>
    <text class="offer" x="1273" y="994" font-size="46">UP TO</text>
    <text class="offer" x="1271" y="1044" font-size="52">$2,000<tspan font-size="30" dx="5" dy="-16">OFF</tspan></text>
    <text class="offer" x="1273" y="1090" font-size="46" textLength="172" lengthAdjust="spacingAndGlyphs">WITH FREE</text>
    <text class="offer" x="1273" y="1127" font-size="36" textLength="172" lengthAdjust="spacingAndGlyphs">CONSULTATION</text>
    <text class="offer" x="1273" y="1171" font-size="46" textLength="172" lengthAdjust="spacingAndGlyphs">AND XRAYS</text>
    <text class="offer" x="1273" y="1203" font-size="28" textLength="174" lengthAdjust="spacingAndGlyphs">TILL JULY 31<tspan font-size="14" dy="-10">ST</tspan><tspan dy="10"> 2020</tspan></text>

    <text class="headline" x="926" y="789" font-size="66" textLength="426" lengthAdjust="spacingAndGlyphs">WHAT BETTER TIME</text>
    <text class="headline" x="926" y="864" font-size="82" textLength="426" lengthAdjust="spacingAndGlyphs">TO GET BRACES</text>
    <text class="headline" x="926" y="898" font-size="28" textLength="426" lengthAdjust="spacingAndGlyphs">WHEN YOU HAVE TO WEAR A MASK ALL THE TIME</text>

    <rect x="867" y="920" width="232" height="235" rx="60" fill="url(#smile-tones)" role="img" aria-label="Illustration of a smiling mouth with a gloved hand holding a dental mirror"/>

    <g class="brand">
      <circle class="brand-dot" cx="935" cy="1265" r="24"/>
      <text class="brand-name" x="995" y="1266" font-size="30" textLength="172" lengthAdjust="spacingAndGlyphs">PINECREST FAMILY DENTISTRY</text>
      <text class="brand-name" x="995" y="1294" font-size="18" textLength="120" lengthAdjust="spacingAndGlyphs">DR MARIAN HOLLOWAY</text>
    </g>
  </g>
</svg>
</body>
</html>
```